A Label for an ECO Friendly Spirit Company

Design a label which can be used for vodka and gin (London Dry Gin). It should be Square type Like the Shape File you see in the uploads. VORK means Local Eco friendly Authentic and Fair. We want a cool and slim label that calls for eco-friendly. We want to use it for our premium
Vodka and our London Dry Gin. Please use the logo and design it in Square Type.

40%vol, 700ml

Target Market(s)

spirits and events

Industry/Entity Type

SPIRITS

Colors
00AB8E
00BBA5
67D7C9
C6EFE9
E9F9F6
59FF00
82FF00
B8FF75
E3FFCB
F4FFEA

Requirements
Must have
• Logo from VORK, Squaee Shape

```html
<!DOCTYPE html>
<html lang="en">
<head>
<meta charset="utf-8">
<title>VORK London Dry Gin Label</title>
<link rel="stylesheet" href="https://fonts.googleapis.com/css2?family=Montserrat:wght@500&family=Open+Sans:wght@400;600&family=Great+Vibes&display=swap">
<style>
  :root {
    --page-bg: #f5f6f8;
    --frame-white: #ffffff;
    --sky: #bfe3ea;
    --lime-soft: #e3f0d2;
    --lime: #c6de8f;
    --teal-soft: #95d3c9;
    --brand-teal: #0e9a80;
    --ink: #2a3a36;
  }
  * { margin: 0; padding: 0; box-sizing: border-box; }
  html, body { width: 1200px; height: 1086px; overflow: hidden; }
  body { background: var(--page-bg); position: relative; font-family: "Open Sans", sans-serif; }

  .label { position: absolute; inset: 0; }
  .label-shape { position: absolute; inset: 0; }

  .label-content {
    position: absolute; inset: 0;
    text-align: center; color: var(--ink);
  }
  .brand-name {
    position: absolute; top: 500px; left: 0; right: 0;
    font-family: "Montserrat", sans-serif; font-weight: 500;
    font-size: 64px; line-height: 1; letter-spacing: 14px;
    color: var(--ink);
  }
  .product-name {
    position: absolute; top: 664px; left: 0; right: 0;
    font-family: "Montserrat", sans-serif; font-weight: 500;
    font-size: 46px; line-height: 1; color: var(--brand-teal);
  }
  .origin {
    position: absolute; top: 730px; left: 0; right: 0;
    font-size: 17px; font-weight: 600; letter-spacing: 1.5px;
  }
  .blend {
    position: absolute; top: 772px; left: 0; right: 0;
    font-family: "Great Vibes", cursive; font-size: 30px; line-height: 1.2;
  }
  .specs {
    position: absolute; top: 832px; left: 0; right: 0;
    font-size: 19px; letter-spacing: 1px;
  }
</style>
</head>
<body>
<main class="label">
  <svg class="label-shape" width="1200" height="1086" viewBox="0 0 1200 1086">
    <defs>
      <linearGradient id="label-fill" x1="0" y1="0" x2="1" y2="1">
        <stop offset="0" stop-color="var(--sky)"/>
        <stop offset="0.45" stop-color="var(--lime-soft)"/>
        <stop offset="0.65" stop-color="var(--lime)"/>
        <stop offset="1" stop-color="var(--teal-soft)"/>
      </linearGradient>
    </defs>
    <polygon class="label-frame" points="600,80 1064,543 600,1006 136,543" fill="var(--frame-white)"/>
    <polygon class="label-field" points="600,110 1033,543 600,976 167,543" fill="url(#label-fill)"
             role="img" aria-label="Soft organic blobs in pale sky blue, lime and mint"/>
  </svg>

  <div class="label-content">
    <p class="brand-name">VORK</p>
    <h1 class="product-name">London Dry Gin</h1>
    <p class="origin">PRODUCED &amp; BOTTLED IN GERMANY</p>
    <p class="blend">Signature Blend</p>
    <p class="specs">40%vol &nbsp;|&nbsp; 700ml</p>
  </div>
</main>
</body>
</html>
```